Harborlane Consultants LLC web site

Harborlane Consultants LLC is a consulting and recruiting firm that provides education, perspective, guidance, and assistance to financial advisors. Dennis Malbrook is the founder of this new firm and is the only employee at this time.
Please see the attached overview which will provide much narrative describing the firm, its purpose, scope of services offered, and other useful information to help you design a web site.

Target Market(s)

US based financial advisors who are looking to transition their business to an independent ( non-employee ) business model.

Industry/Entity Type

Consultant

Coding

Coded - Design and coding required

Number of Pages Required

5+ page

Font styles to use
Sans Serif

Requirements
Must have
• all relevant pages for a basic web site : Home, About, Services offered, Contact, Resources , etc.
Nice to have
• color scheme : see logo in the attached briefing document

```html
<!DOCTYPE html>
<html lang="en">
<head>
<meta charset="utf-8">
<title>Harborlane Consultants LLC</title>
<link rel="stylesheet" href="https://fonts.googleapis.com/css2?family=Arimo:wght@400;700&family=Roboto+Slab:wght@400;500;600&display=swap">
<style>
:root{
  --navy:#0f3e6c;
  --navy-dark:#0a2d50;
  --ice:#a9c2d8;
  --ink:#111;
  --muted:#444;
  --field:#e3e3e3;
  --white:#fff;
  --footer:#000;
  --sky-top:#5f86b3;
  --sea:#1d4f86;
}
*{box-sizing:border-box;margin:0;padding:0}
html,body{width:1200px;height:4095px;overflow:hidden}
body{position:relative;background:var(--white);font-family:"Arimo",Arial,sans-serif;color:var(--ink)}
.abs{position:absolute}
.slab{font-family:"Roboto Slab",Georgia,serif}
.btn{position:absolute;display:flex;align-items:center;justify-content:center;gap:9px;border-radius:20px;font-family:"Roboto Slab",Georgia,serif;font-weight:600;font-size:15px;letter-spacing:1px}
.btn-light{background:var(--white);color:var(--navy)}
.btn-navy{background:var(--navy);color:var(--white)}
.btn .dot{width:13px;height:13px;border-radius:50%;background:currentColor;position:relative}
.btn-light .dot::after,.btn-navy .dot::after{content:"";position:absolute;left:4px;top:3px;border-left:6px solid var(--white);border-top:3.5px solid transparent;border-bottom:3.5px solid transparent}
.btn-light .dot::after{border-left-color:var(--white)}
.btn-navy .dot::after{border-left-color:var(--navy)}

/* hero */
.hero{left:0;top:0;width:1200px;height:601px;background:linear-gradient(180deg,#6f93bd 0%,#a9bfd6 38%,#3b6a9c 58%,#1d4a7c 80%,#4d5a46 100%)}
.brand{display:flex;align-items:center;gap:12px;font-family:"Roboto Slab",Georgia,serif;font-weight:500;font-size:19px;letter-spacing:1px}
.brand .mark{width:40px;height:40px;border-radius:50%;border:3px solid currentColor}
.hero .brand{position:absolute;left:111px;top:16px;color:var(--white)}
.nav{position:absolute;top:26px;left:520px;display:flex;gap:34px;font-size:14px;color:var(--white)}
.social{position:absolute;display:flex;gap:12px}
.social i{display:block;width:11px;height:11px;border-radius:50%;background:currentColor}
.hero-title{left:111px;top:214px;color:var(--white);font-size:41px;line-height:49px;font-weight:500}
.hero-sub{left:111px;top:324px;width:320px;color:var(--white);font-size:13.5px;line-height:24px}

/* about */
.portrait{left:111px;top:690px;width:293px;height:359px;background:linear-gradient(160deg,#4a4a4a,#2e3440 60%,#5d6f8f)}
.frame{left:404px;top:733px;width:166px;height:142px;border:7px solid #6f8eac;border-left:none;border-bottom:none}
.chart-card{left:257px;top:879px;width:360px;height:227px;background:#f6f7f8;box-shadow:0 2px 10px rgba(0,0,0,.12)}
.eyebrow{color:var(--navy);font-size:14.5px}
.h2{font-family:"Roboto Slab",Georgia,serif;font-weight:500;font-size:35px;color:var(--ink)}
.about-text{left:656px;top:834px;width:440px;font-size:13.5px;line-height:30px;color:var(--muted)}

/* services */
.service{top:1317px;height:521px;display:flex;align-items:flex-end;padding:0 0 30px 14px;color:var(--white);font-weight:700;font-size:22px;letter-spacing:.5px}
.arrow{position:absolute}

/* testimonials */
.avatar{position:absolute;border-radius:50%}
.quote{left:647px;top:2108px;width:460px;font-size:14.5px;line-height:37px;color:var(--muted)}

/* banner */
.banner{left:0;top:2446px;width:1200px;height:454px;background:linear-gradient(180deg,#8fb0c9 0%,#2c6e9c 18%,#1a5a8a 55%,#0f3f6b 100%)}

/* contact */
.label{position:absolute;font-family:"Roboto Slab",Georgia,serif;font-weight:600;font-size:18px;color:var(--ink)}
.field{position:absolute;background:var(--field);color:#888;font-size:13px;padding:24px 24px}

/* footer */
.footer{left:0;top:3752px;width:1200px;height:343px;background:var(--footer);color:var(--white)}
.fhead{position:absolute;top:73px;font-family:"Roboto Slab",Georgia,serif;font-weight:600;font-size:19px;letter-spacing:1px}
.flinks{position:absolute;top:104px;font-size:14px;line-height:30px}
</style>
</head>
<body>

<!-- Hero -->
<section class="abs hero" role="img" aria-label="Photo of a lighthouse on a grassy rocky point above the sea under a blue cloudy sky"></section>
<div class="brand"style="position:absolute;left:111px;top:16px;color:#fff"><span class="mark"></span>Harborlane Consultants LLC</div>
<nav class="nav"><span>Home</span><span>About</span><span>Services offered</span><span>Contact</span><span>Resources</span></nav>
<div class="social" style="left:992px;top:31px;color:#fff"><i></i><i></i><i></i><i></i></div>
<h1 class="abs slab hero-title">HARBORLANE<br>CONSULTANTS LLC</h1>
<p class="abs hero-sub">helping financial advisors to navigate their journey to independence</p>
<div class="btn btn-light" style="left:111px;top:394px;width:170px;height:38px">LEARN MORE <span class="dot"></span></div>

<!-- About -->
<div class="abs portrait" role="img" aria-label="Portrait photo of the founder in a light striped shirt"></div>
<div class="abs frame"></div>
<div class="abs chart-card">
  <svg width="360" height="227" viewBox="0 0 360 227">
    <g fill="#1f7fb8">
      <rect x="15" y="30" width="5" height="25"/><rect x="24" y="20" width="5" height="35"/><rect x="33" y="35" width="5" height="20"/><rect x="42" y="15" width="5" height="40"/><rect x="51" y="28" width="5" height="27"/>
      <rect x="120" y="25" width="5" height="30"/><rect x="129" y="18" width="5" height="37"/><rect x="138" y="30" width="5" height="25"/>
      <rect x="15" y="100" width="5" height="30"/><rect x="24" y="92" width="5" height="38"/><rect x="33" y="106" width="5" height="24"/>
    </g>
    <g fill="#28b7a3">
      <rect x="200" y="20" width="5" height="35"/><rect x="209" y="28" width="5" height="27"/><rect x="218" y="34" width="5" height="21"/><rect x="227" y="38" width="5" height="17"/>
      <rect x="300" y="30" width="5" height="25"/><rect x="309" y="24" width="5" height="31"/><rect x="318" y="32" width="5" height="23"/>
    </g>
    <polyline points="90,120 105,100 118,115 132,95 148,118 160,104" fill="none" stroke="#28b7a3" stroke-width="2"/>
    <polygon points="200,125 220,110 240,118 262,100 262,130 200,130" fill="#28b7a3" opacity=".7"/>
    <polyline points="120,200 135,170 150,195 165,160 180,198 195,175 210,190" fill="none" stroke="#1f7fb8" stroke-width="2"/>
    <g fill="#3ecf9b">
      <rect x="15" y="160" width="80" height="5" rx="2"/><rect x="15" y="175" width="60" height="5" rx="2"/><rect x="15" y="190" width="90" height="5" rx="2"/>
      <rect x="300" y="165" width="45" height="5" rx="2"/><rect x="300" y="180" width="35" height="5" rx="2"/><rect x="300" y="195" width="40" height="5" rx="2"/>
    </g>
  </svg>
</div>
<p class="abs eyebrow" style="left:656px;top:750px">About us</p>
<h2 class="abs h2" style="left:656px;top:778px">Dennis Malbrook</h2>
<p class="abs about-text">Harborlane Consultants LLC is a consulting and recruiting firm that provides education,perspective, guidance, and assistance to financial advisors.Specifically, we are focused on serving two distinct profiles of client First, we assist financial advisors as they explore, plan, and execute their professional journey to</p>
<div class="btn btn-navy" style="left:656px;top:1004px;width:170px;height:38px">LEARN MORE <span class="dot"></span></div>

<!-- Services -->
<p class="abs eyebrow" style="left:111px;top:1204px">OUR SERVICES</p>
<h2 class="abs h2" style="left:111px;top:1228px">What Steady Course Do</h2>
<svg class="arrow" style="left:1022px;top:1243px" width="66" height="16" viewBox="0 0 66 16"><g stroke="#111" stroke-width="2.5" fill="none"><path d="M2 8h20M8 3L2 8l6 5"/><path d="M44 8h20M58 3l6 5-6 5"/></g></svg>
<div class="abs service" style="left:0;width:386px;background:linear-gradient(160deg,#7fc6cf,#c3dde0 55%,#3d6f82)" role="img" aria-label="Photo of a compass resting on a map">EDUCATION</div>
<div class="abs service" style="left:407px;width:384px;background:linear-gradient(170deg,#5b7a4a,#2f9ea6 45%,#1ab0bf 75%,#137f94)" role="img" aria-label="Aerial photo of boats in a turquoise bay">PERSPECTIVE</div>
<div class="abs service" style="left:812px;width:388px;background:linear-gradient(180deg,#7a6f6e,#c49a80 35%,#3a3b44 70%,#1f2430)" role="img" aria-label="Photo of sailboats moored in a marina at sunset">GUIDANCE</div>

<!-- Testimonials -->
<p class="abs eyebrow" style="left:0;width:1167px;text-align:center;top:1921px">OUR TESTIMONIALS</p>
<h2 class="abs h2" style="left:0;width:1200px;text-align:center;top:1951px">What Our Clients Have To Say</h2>
<div class="avatar" style="left:135px;top:2064px;width:86px;height:86px;background:#b9b6b2" role="img" aria-label="Client photo"></div>
<div class="avatar" style="left:41px;top:2221px;width:112px;height:112px;background:#a98e80" role="img" aria-label="Client photo"></div>
<div class="avatar" style="left:232px;top:2272px;width:86px;height:86px;background:#c7bcb3" role="img" aria-label="Client photo"></div>
<svg class="abs" style="left:290px;top:2018px" width="336" height="336" viewBox="0 0 336 336">
  <circle cx="168" cy="168" r="160" fill="none" stroke="#9ab4cc" stroke-width="9"/>
  <polygon points="40,50 75,45 55,80" fill="#9ab4cc"/>
  <polygon points="300,250 295,300 260,285" fill="#9ab4cc"/>
</svg>
<div class="avatar" style="left:310px;top:2038px;width:296px;height:296px;background:radial-gradient(circle at 50% 45%,#b8a89a,#7d7e80 70%,#5a5c60)" role="img" aria-label="Photo of a young man in a suit"></div>
<p class="abs quote">Lorem ipsum dolor sit amet, consectetur adipiscing elit, sed do eiusmod tempor incididunt ut labore et dolore magna aliqua. Quis ipsum suspendisse ultrices gravida.</p>
<p class="abs" style="left:647px;top:2235px;font-size:14.5px;font-weight:700"><span style="color:var(--navy)">Marcus Ellery</span>&nbsp;&nbsp; Advisor</p>
<div class="abs" style="left:928px;top:2315px;width:64px;height:38px;background:#fff;box-shadow:0 2px 8px rgba(0,0,0,.2)"></div>
<svg class="arrow" style="left:950px;top:2327px" width="20" height="14" viewBox="0 0 20 14"><path d="M2 7h17M7 2L2 7l5 5" stroke="#111" stroke-width="2.5" fill="none"/></svg>
<svg class="arrow" style="left:1033px;top:2327px" width="18" height="14" viewBox="0 0 18 14"><path d="M1 7h15M11 3l5 4-5 4" stroke="#666" stroke-width="1.6" fill="none"/></svg>

<!-- Banner -->
<section class="abs banner" role="img" aria-label="Photo of a sailboat with a striped sail racing on open blue sea"></section>
<h2 class="abs slab" style="left:113px;top:2544px;color:#fff;font-size:35px;line-height:46px;font-weight:500">Steady Course Is<br>Harborlane Consultants<br>LLC</h2>
<p class="abs" style="left:114px;top:2709px;color:#fff;font-size:13px">Lorem ipsum dolor sit amet, consectetur adipiscing elit</p>
<div class="btn btn-navy" style="left:114px;top:2754px;width:170px;height:38px">LEARN MORE <span class="dot"></span></div>

<!-- Contact -->
<p class="abs eyebrow" style="left:0;width:1169px;text-align:center;top:2987px">CONTACT US</p>
<h2 class="abs h2" style="left:0;width:1169px;text-align:center;top:3014px">Get In Touch</h2>
<span class="label" style="left:232px;top:3113px">Tell us your name</span>
<span class="label" style="left:619px;top:3113px">Enter your email</span>
<div class="field" style="left:230px;top:3154px;width:350px;height:59px">Enter your name</div>
<div class="field" style="left:618px;top:3154px;width:350px;height:59px">Enter your email</div>
<span class="label" style="left:233px;top:3245px">Your website</span>
<div class="field" style="left:232px;top:3286px;width:736px;height:59px">http://</div>
<span class="label" style="left:233px;top:3381px">Message</span>
<div class="field" style="left:232px;top:3423px;width:736px;height:151px;padding-top:20px">Your message here</div>
<div class="btn btn-navy" style="left:528px;top:3615px;width:143px;height:40px">SUBMIT <span class="dot"></span></div>

<!-- Footer -->
<footer class="abs footer">
  <div class="brand" style="position:absolute;left:111px;top:68px;color:var(--navy);font-size:17px"><span class="mark"></span>Harborlane Consultants LLC</div>
  <p style="position:absolute;left:112px;top:140px;width:250px;font-size:14px;line-height:30px">Lorem ipsum dolor sit amet, consectetur adipiscing elit, sed do eiusmod tempor incididunt ut labore</p>
  <h3 class="fhead" style="left:429px">QUICK LINK</h3>
  <div class="flinks" style="left:432px">Home<br>About<br>Services offered<br>Contact<br>Resources</div>
  <h3 class="fhead" style="left:639px">HELP LINK</h3>
  <div class="flinks" style="left:641px">Terms &amp; Conditions<br>Privacy Policy<br>Terms of Sales</div>
  <h3 class="fhead" style="left:872px">SUBSCRIBE</h3>
  <svg style="position:absolute;left:873px;top:112px" width="16" height="12" viewBox="0 0 16 12"><rect x="1" y="1" width="14" height="10" fill="none" stroke="#ccc" stroke-width="1.3"/><path d="M1 1l7 5 7-5" fill="none" stroke="#ccc" stroke-width="1.3"/></svg>
  <span style="position:absolute;left:898px;top:110px;font-size:14px;color:#ccc">Email</span>
  <svg style="position:absolute;left:1068px;top:110px" width="16" height="16" viewBox="0 0 16 16"><path d="M1 8l14-7-4 14-3-5z" fill="none" stroke="var(--navy)" stroke-width="1.3"/></svg>
  <div style="position:absolute;left:872px;top:136px;width:214px;height:1px;background:#ccc"></div>
  <div class="social" style="left:874px;top:172px;color:#fff"><i></i><i></i><i></i><i></i></div>
  <p style="position:absolute;left:0;width:1200px;text-align:center;top:298px;font-size:14px">©Copyrights 2021 Harborlane Consultants LLC &nbsp; | &nbsp; All Rights Reserved</p>
</footer>

</body>
</html>
```